Professional window cleaning services business needs a flyer design

We are looking to attract large businesses such as gyms, car dealerships and fast food restaurants.
-Have over 15 years of experience in this business
-We serve customers in Melbourne and all surrounding suburbs
-Specialising in automated periodical services(daily,weekly,monthly, yearly)
-Our current client base consists of major fast food restaurants, car dealerships and residential properties.

Industry/Entity Type

Window Cleaning

Colors
3176b5
fbed22

Requirements
Must have
• Business Details:
• Name: Brightpane Window Cleaning
• Phone no:95402367
• website:www.quorlinpro.com.au
• email: admin@quorlinpro.com.au
• mail: PO BOX 4826, Marrowdale Heights, 3478

```html
<!DOCTYPE html>
<html lang="en">
<head>
<meta charset="utf-8">
<title>Brightpane Window Cleaning Flyer</title>
<link href="https://fonts.googleapis.com/css2?family=Oswald:wght@400;500&family=Open+Sans:wght@400;600&family=Roboto+Condensed:ital,wght@0,400;0,700;1,700&family=Lato:wght@400&display=swap" rel="stylesheet">
<style>
  :root {
    --brand-blue: #3176b5;
    --deep-blue: #1c4ea8;
    --brand-yellow: #fbed22;
    --sun-yellow: #f7e300;
    --ink: #1e1e1e;
    --charcoal: #2b2b2b;
    --paper: #ffffff;
    --backdrop: #e9e9e9;
  }
  * { margin: 0; padding: 0; box-sizing: border-box; }
  html, body {
    width: 907px; height: 1200px; overflow: hidden;
    background: var(--backdrop);
  }
  .flyer {
    position: absolute; left: 93px; top: 103px;
    width: 726px; height: 1016px;
    background: var(--paper);
    overflow: hidden;
    box-shadow: 0 4px 14px rgba(0,0,0,.25);
  }
  .flyer-shapes { position: absolute; inset: 0; }
  .brand-name {
    position: absolute; left: 22px; top: 60px;
    font-family: 'Oswald', sans-serif; font-weight: 500;
    font-size: 36px; letter-spacing: 1px;
    color: var(--brand-blue);
  }
  .headline {
    position: absolute; left: 24px; top: 534px; width: 390px;
    font-family: 'Oswald', sans-serif; font-weight: 500;
    font-size: 30px; line-height: 1; color: var(--ink);
    white-space: nowrap;
  }
  .headline .accent { color: var(--brand-blue); }
  .staff-note {
    position: absolute; left: 24px; top: 590px;
    font-family: 'Oswald', sans-serif; font-weight: 500;
    font-size: 19px; color: var(--ink); white-space: nowrap;
  }
  .experience {
    position: absolute; left: 0; top: 644px; width: 419px;
    text-align: center;
    font-family: 'Lato', sans-serif; font-size: 25px; line-height: 33px;
    color: var(--ink);
  }
  .experience .years {
    font-family: 'Oswald', sans-serif; font-weight: 400;
    color: var(--brand-blue); font-size: 25px;
  }
  .quote-offer {
    position: absolute; left: 20px; top: 798px;
    font-family: 'Roboto Condensed', sans-serif; font-weight: 700;
    font-size: 26px; color: var(--deep-blue);
  }
  .call-now {
    position: absolute; left: 22px; top: 842px;
    font-family: 'Lato', sans-serif; font-size: 24px; color: var(--ink);
  }
  .phone {
    position: absolute; left: 20px; top: 876px;
    font-family: 'Lato', sans-serif; font-size: 34px; color: var(--ink);
  }
  .website {
    position: absolute; left: 0; top: 970px; width: 726px;
    text-align: center;
    font-family: 'Open Sans', sans-serif; font-weight: 600;
    font-size: 15px; color: var(--paper);
  }
  .panel-tab {
    position: absolute; right: 0;
    background: var(--sun-yellow);
    font-family: 'Roboto Condensed', sans-serif; font-weight: 400;
    font-size: 17px; color: var(--ink);
    padding: 0 10px 0 13px; height: 23px; line-height: 23px;
    border-radius: 12px 0 0 12px;
  }
  .tab-about { top: 467px; }
  .tab-services { top: 734px; }
  .about-copy {
    position: absolute; left: 423px; top: 502px; width: 282px;
    font-family: 'Open Sans', sans-serif; font-size: 10px;
    line-height: 12.6px; color: var(--paper); text-align: justify;
  }
  .about-copy p { margin-bottom: 8px; }
  .service-list {
    position: absolute; top: 771px; list-style: none;
    font-family: 'Open Sans', sans-serif; font-size: 10.5px;
    line-height: 21px; color: var(--paper); text-align: right;
  }
  .service-list li::after {
    content: ""; display: inline-block; width: 9px; height: 9px;
    border-radius: 50%; background: var(--brand-yellow);
    margin-left: 9px; vertical-align: -1px;
  }
  .service-list .two-line { line-height: 13px; padding: 4px 0 4px; }
  .services-left { left: 420px; width: 112px; }
  .services-right { left: 540px; width: 170px; }
  .frequency {
    position: absolute; left: 419px; top: 890px; width: 307px;
    text-align: center;
    font-family: 'Roboto Condensed', sans-serif; font-weight: 700; font-style: italic;
    font-size: 19.5px; line-height: 22px; color: var(--brand-yellow);
  }
</style>
</head>
<body>
<main class="flyer">
  <svg class="flyer-shapes" width="726" height="1016" viewBox="0 0 726 1016">
    <defs>
      <linearGradient id="photoTones" x1="0" y1="0" x2="0" y2="1">
        <stop offset="0" stop-color="#7f93bd"/>
        <stop offset="0.45" stop-color="#b9c4d6"/>
        <stop offset="0.8" stop-color="#8a9a8a"/>
        <stop offset="1" stop-color="#4c5e3e"/>
      </linearGradient>
      <linearGradient id="bandYellow" x1="0" y1="0" x2="0" y2="1">
        <stop offset="0" stop-color="#f7e600"/>
        <stop offset="0.5" stop-color="#fff7a8"/>
        <stop offset="1" stop-color="#f7e600"/>
      </linearGradient>
      <linearGradient id="panelTone" x1="0" y1="0" x2="1" y2="1">
        <stop offset="0" stop-color="#2f6fd6"/>
        <stop offset="1" stop-color="#1d4fb0"/>
      </linearGradient>
    </defs>
    <rect class="info-panel" x="419" y="380" width="307" height="575" fill="url(#panelTone)"/>
    <path role="img" aria-label="Photo of a worker cleaning the glass facade of an office building with a pole, a branded van parked beside it"
      d="M0,170 C120,190 250,120 310,0 L726,0 L726,360 C600,410 440,470 300,466 C180,462 80,390 0,282 Z"
      fill="url(#photoTones)"/>
    <path d="M0,0 L350,0 C300,130 160,215 0,205 Z" fill="var(--brand-blue)"/>
    <path d="M0,0 L332,0 C282,122 150,205 0,196 Z" fill="var(--sun-yellow)"/>
    <path d="M0,0 L316,0 C268,115 140,195 0,188 Z" fill="var(--ink)"/>
    <path d="M0,0 L304,0 C256,110 132,188 0,180 Z" fill="var(--paper)"/>
    <path d="M0,282 C80,390 180,462 300,466 C440,470 600,410 726,355 L726,388 C600,442 440,496 300,494 C180,492 80,420 0,338 Z" fill="var(--sun-yellow)"/>
    <path d="M0,282 C80,390 180,462 300,466 C440,470 600,410 726,355 L726,366 C600,420 440,480 300,478 C185,476 85,405 0,306 Z" fill="var(--ink)"/>
    <rect x="0" y="637" width="419" height="115" fill="url(#bandYellow)"/>
    <path d="M0,928 C250,938 500,948 726,930 L726,975 L0,975 Z" fill="var(--brand-blue)"/>
    <path d="M0,944 C250,950 500,958 726,945 L726,985 L0,985 Z" fill="var(--sun-yellow)"/>
    <path d="M0,962 C250,958 500,966 726,955 L726,1016 L0,1016 Z" fill="var(--charcoal)"/>
  </svg>

  <div class="brand-name">BRIGHTPANE</div>

  <h1 class="headline"><span class="accent">BRIGHTPANE WINDOW</span> CLEANING</h1>
  <p class="staff-note">OUR STAFF ARE FULLY TRAINED AND UNIFORMED</p>

  <p class="experience">We Have<br><span class="years">OVER 15 YEARS OF EXPERIENCE</span><br>In this business</p>

  <p class="quote-offer">Free Window Cleaning Quote</p>
  <p class="call-now">Call Us Now</p>
  <p class="phone">(03) 9540 2367</p>

  <div class="panel-tab tab-about">About Us</div>
  <div class="about-copy">
    <p>Brightpane Services started trading in 1999 with a clear focus on becoming a market leader in the Window Cleaning Industry. Since then we have proudly built the business based on strong ethical standards, focused on customer service.</p>
    <p>With this viewpoint in mind we have built a reputation for fast, efficient service that has paved the way for us to become one of the leaders in window cleaning in Melbourne. Our clients now range from big corporate jobs such as stadiums and office buildings, to shop fronts to residential. Our scaled pricing allows us to be competitive in all markets.</p>
    <p>By continually improving our high quality standards and our strong customer focus, we aim to continue our growth within Victoria and into other states.</p>
  </div>

  <div class="panel-tab tab-services">Our Services</div>
  <ul class="service-list services-left">
    <li>Pressure Cleaning</li>
    <li>Blind Cleaning</li>
    <li class="two-line">Roof Repairs &amp;<br>Roof Cleaning</li>
    <li>Consulting</li>
  </ul>
  <ul class="service-list services-right">
    <li>Residential Window Cleaning</li>
    <li>Commercial Window Cleaning</li>
    <li>Real Estate Window Cleaning</li>
    <li>High Rise Window Cleaning</li>
    <li>Gutter Cleaning</li>
  </ul>

  <p class="frequency">Daily,Weekly,Monthly, Yearly<br>Service Available</p>

  <p class="website">www.quorlinpro.com.au</p>
</main>
</body>
</html>
```